Card and board game developer website, small e-commerce site

We are designing a website for Copper Lantern Otter Works. I need a homepage and a typical inside page designed.
The website navigation will be:
Home (where we'll introduce the games and the website)
Our Games (drops open into the two games)
Griffins of Morvale Keep
Tidecraft
Order Now
About Us
Contact
The header of the website will include the logo, the navigation and a link to a facebook page. The header will also include a cart icon and a link to My Account.
Then on the homepage I suggest we include a row for each game:
Griffins of Morvale Keep
This row will include a photo (or maybe a series of photos that animate into each other) and quick info about the game plus two buttons: Info and Photos (which will go to the detail page with the photo gallery), and Order Now (which will take you to the product for ordering).
Tidecraft
Your footer will contain a copyright note, plus links to:
Terms and conditions
Shipping and returns
FAQ
Contact
Account login
NOTE: the logo is the orange mokey. I've uploaded a brief with more information. The current website that we are redesigning is here https://www.copperlanternotter.example/
Please send me any questions that you have.
Target Market(s)
People interested in fun card and board games at home.
Number of Pages Required
Look and feel

```html
<!DOCTYPE html>
<html lang="en">
<head>
<meta charset="utf-8">
<title>About Us – Copper Lantern Otter Works</title>
<link href="https://fonts.googleapis.com/css2?family=Fira+Sans:wght@500;600&family=Open+Sans:wght@400;600&display=swap" rel="stylesheet">
<style>
  :root {
    --orange: #f08a24;
    --ink: #222222;
    --header-bg: #f9f9f9;
    --hero-bg: #f0efee;
    --ghost: rgba(0,0,0,0.035);
    --white: #ffffff;
  }
  * { box-sizing: border-box; margin: 0; padding: 0; }
  html, body { width: 1200px; height: 1104px; overflow: hidden; }
  body { background: var(--white); font-family: "Open Sans", sans-serif; color: var(--ink); position: relative; }

  .site-header { position: absolute; top: 0; left: 0; width: 1200px; height: 86px; background: var(--header-bg); }
  .brand { position: absolute; left: 106px; top: 14px; display: flex; align-items: center; gap: 8px; width: 150px; }
  .brand-dot { width: 14px; height: 14px; border-radius: 50%; background: var(--orange); flex: none; }
  .brand-name { font-family: "Open Sans", sans-serif; font-weight: 600; font-size: 13px; line-height: 16px; color: var(--orange); text-transform: uppercase; }

  .main-nav { position: absolute; left: 391px; top: 31px; display: flex; gap: 24px; font-size: 16px; }
  .main-nav a { color: var(--ink); text-decoration: none; }
  .main-nav a.is-active { color: var(--orange); }

  .header-tools { position: absolute; left: 968px; top: 28px; display: flex; gap: 16px; align-items: center; }
  .cart-count { position: absolute; left: 101px; top: -2px; width: 17px; height: 17px; border-radius: 50%; background: var(--orange); color: var(--ink); font-size: 10px; text-align: center; line-height: 17px; }

  .hero { position: absolute; top: 86px; left: 0; width: 1200px; height: 742px; background: var(--hero-bg); overflow: hidden; }
  .ghost-title { position: absolute; left: 450px; top: 40px; font-family: "Fira Sans", sans-serif; font-weight: 600; color: var(--ghost); white-space: nowrap; line-height: 0.95; text-transform: uppercase; }
  .ghost-title span { display: block; font-size: 110px; }

  .hero-art { position: absolute; left: 111px; top: 101px; width: 385px; height: 546px; background: linear-gradient(180deg, #3c5fa8 0%, #b8461e 28%, #c9c4bd 52%, #4f8a35 75%, #3b6f2f 100%); box-shadow: 0 6px 14px rgba(0,0,0,0.25); }

  .hero-copy { position: absolute; left: 542px; top: 106px; width: 560px; }
  .eyebrow { font-family: "Fira Sans", sans-serif; font-weight: 600; font-size: 40px; line-height: 1; color: var(--orange); }
  .page-title { font-family: "Fira Sans", sans-serif; font-weight: 600; font-size: 56px; line-height: 63px; color: var(--orange); margin-top: 8px; text-transform: uppercase; }
  .lead { font-size: 17px; margin-top: 32px; }
  .body-text { font-size: 17px; line-height: 28.5px; margin-top: 16px; }
  .cta-line { font-size: 17px; font-weight: 600; margin-top: 20px; }
  .btn-order { display: inline-block; margin-top: 50px; margin-left: -2px; width: 140px; height: 47px; background: var(--orange); color: var(--white); font-weight: 600; font-size: 16px; text-align: center; line-height: 47px; text-decoration: none; }

  .site-footer { position: absolute; top: 828px; left: 0; width: 1200px; height: 276px; background: var(--white); text-align: center; }
  .footer-brand { position: absolute; left: 520px; top: 52px; width: 160px; display: flex; align-items: center; justify-content: center; gap: 8px; }
  .footer-links { position: absolute; top: 188px; left: 0; width: 1200px; display: flex; justify-content: center; gap: 28px; font-size: 17px; }
  .footer-links a { color: var(--ink); text-decoration: none; }
  .copyright { position: absolute; top: 224px; left: 0; width: 1200px; font-size: 17px; }
</style>
</head>
<body>
  <header class="site-header">
    <a class="brand" href="#"><span class="brand-dot"></span><span class="brand-name">Copper Lantern Otter Works</span></a>
    <nav class="main-nav">
      <a href="#">Home</a>
      <a href="#">Our Games</a>
      <a href="#">Order Now</a>
      <a href="#" class="is-active">About Us</a>
      <a href="#">Contact</a>
    </nav>
    <div class="header-tools">
      <svg width="26" height="26" viewBox="0 0 26 26" aria-label="Social page"><circle cx="13" cy="13" r="11.5" fill="none" stroke="#222" stroke-width="1.6"/></svg>
      <svg width="26" height="26" viewBox="0 0 26 26" aria-label="My account"><circle cx="13" cy="13" r="11.5" fill="none" stroke="#222" stroke-width="1.8"/><circle cx="13" cy="10" r="4.2" fill="#222"/><path d="M5.5 20.5c2-4 13-4 15 0" fill="#222"/></svg>
      <svg width="30" height="26" viewBox="0 0 30 26" aria-label="Cart"><path d="M1 3h5l3.5 14h15l3-10H8" fill="none" stroke="#222" stroke-width="1.8" stroke-linejoin="round"/><circle cx="11" cy="22" r="2" fill="none" stroke="#222" stroke-width="1.6"/><circle cx="23" cy="22" r="2" fill="none" stroke="#222" stroke-width="1.6"/></svg>
      <span class="cart-count">2</span>
    </div>
  </header>

  <section class="hero">
    <div class="ghost-title" aria-hidden="true"><span>About Us</span><span>Copper Lantern</span><span>Otter Works</span></div>
    <div class="hero-art" role="img" aria-label="Painted game artwork of a great red winged beast above snowy peaks, castles and green fields"></div>
    <div class="hero-copy">
      <p class="eyebrow">ABOUT US</p>
      <h1 class="page-title">Copper Lantern<br>Otter Works</h1>
      <p class="lead">They say do what you love…</p>
      <p class="body-text">At Copper Lantern Otter Works we love to dream big dreams and bring those dreams to life. We create games to entertain and engage the people that play them; games that invite and inspire players to add a bit of themselves to each game, and how it is played.</p>
      <p class="cta-line">Come play with us.</p>
      <a class="btn-order" href="#">ORDER NOW</a>
    </div>
  </section>

  <footer class="site-footer">
    <div class="footer-brand"><span class="brand-dot"></span><span class="brand-name">Copper Lantern Otter Works</span></div>
    <nav class="footer-links">
      <a href="#">Terms and conditions</a>
      <a href="#">Shipping and returns</a>
      <a href="#">FAQ</a>
      <a href="#">Contact</a>
      <a href="#">Account login</a>
    </nav>
    <p class="copyright">2024 Copper Lantern Otter Works. All Rights Reserved.</p>
  </footer>
</body>
</html>
```